PRV/ Tarnwell Wood/ BSK Corporate Day - Thursday 15th May 2025

A5 Size Invitation printed front and back:
Our Company Colour is British Racing Green
INVITATION FRONT:
Background Pictures Attached:
PRV Lumber Ltd
The Quiet Harbour of Rare Grainstock
PRV Lumber/ Tarnwell Wood/ BSK Corporate Day
Thursday 15th May 2025
www.prvlumber-example.co.uk
sales@prvlumber-example.co.uk
+44 (0) 20 7946 0817
INVITATION BACK:
Golf - sponsored by Tarnwell Wood - Fennock Golf Club, Surrey
Off Road Adventure - sponsored by BSK - Address TBC
Followed by Dinner and Overnight Accommodation at
Brimwell Manor Hotel & Country Club, Surrey
We hope you will be able to join us

```html
<!DOCTYPE html>
<html lang="en">
<head>
<meta charset="utf-8">
<title>Corporate Day Invitation – Back</title>
<link href="https://fonts.googleapis.com/css2?family=Source+Sans+3:ital,wght@0,300;0,400;0,600;0,700;1,300;1,400&display=swap" rel="stylesheet">
<style>
  :root {
    --page: #ffffff;
    --racing-green: #0f2e17;
    --racing-green-deep: rgba(8, 34, 14, 0.82);
    --green-panel: rgba(18, 60, 26, 0.55);
    --green-edge: #1e6b2c;
    --ink-light: #ffffff;
    --photo-sky: #55664f;
    --photo-hills: #33502f;
    --photo-grass: #3d6a33;
    --photo-sand: #6e6238;
  }
  * { box-sizing: border-box; margin: 0; padding: 0; }
  html, body { width: 1200px; height: 1000px; overflow: hidden; background: var(--page); }
  body { font-family: "Source Sans 3", sans-serif; color: var(--ink-light); position: relative; }

  .invitation {
    position: absolute; left: 316px; top: 98px; width: 568px; height: 804px;
    overflow: hidden;
  }
  .venue-photo {
    position: absolute; inset: 0;
    background:
      radial-gradient(ellipse 40% 18% at 10% 80%, rgba(140,120,70,0.55), transparent 70%),
      radial-gradient(ellipse 35% 20% at 90% 80%, rgba(140,120,70,0.55), transparent 70%),
      linear-gradient(180deg, var(--photo-sky) 0%, var(--photo-hills) 22%, #2f4a2a 38%, var(--photo-grass) 55%, #3a5f2e 75%, var(--photo-sand) 100%);
  }
  .venue-photo::after {
    content: ""; position: absolute; inset: 0; background: rgba(10, 40, 16, 0.35);
  }
  .frame {
    position: absolute; left: 23px; top: 24px; right: 23px; bottom: 23px;
    border: 1.5px solid rgba(255,255,255,0.9);
  }

  .sponsor { position: absolute; color: var(--ink-light); font-weight: 700; white-space: nowrap; }
  .sponsor--host { left: 49px; top: 80px; font-size: 36px; letter-spacing: 1px; }
  .sponsor--wood { left: 234px; top: 86px; font-size: 21px; display: flex; align-items: center; gap: 7px; }
  .sponsor--wood .mark { width: 12px; height: 12px; border-radius: 50%; background: var(--ink-light); }
  .sponsor--acoustic { left: 420px; top: 78px; font-size: 38px; letter-spacing: 1px; }

  .events { position: absolute; left: 51px; width: 468px; }
  .band { background: var(--racing-green-deep); border: 1px solid var(--green-edge); }
  .events-title {
    top: 294px; height: 49px; padding-left: 14px;
    font-size: 34px; font-weight: 400; line-height: 47px;
  }
  .event-head {
    display: flex; justify-content: space-between; align-items: center;
    height: 35px; padding: 0 15px;
  }
  .event-name { font-size: 22px; font-weight: 700; }
  .event-sponsor { font-size: 21px; font-style: italic; font-weight: 400; }
  .event-place {
    display: flex; align-items: center; gap: 9px;
    height: 46px; padding-left: 15px;
    background: var(--green-panel); border: 1px solid var(--green-edge); border-top: none;
    font-size: 20px; font-weight: 300;
  }
  .event-place svg { width: 13px; height: 16px; flex: none; }
  .event--golf { top: 357px; }
  .event--offroad { top: 453px; }
  .event--offroad .event-head { height: 45px; }

  .closing {
    top: 558px; height: 165px; padding: 12px 15px 0;
    background: rgba(40, 50, 25, 0.45); border: 1px solid var(--green-edge);
  }
  .closing-details { font-size: 19.5px; font-weight: 300; line-height: 26px; letter-spacing: 0.3px; }
  .closing-wish { margin-top: 22px; font-size: 30px; font-style: italic; font-weight: 300; letter-spacing: -0.3px; }

  .contact-phone {
    position: absolute; left: 0; right: 0; top: 736px;
    display: flex; justify-content: center; align-items: center; gap: 8px;
    font-size: 14px; font-weight: 400;
  }
  .contact-phone svg { width: 15px; height: 15px; }
</style>
</head>
<body>
  <main class="invitation">
    <div class="venue-photo" role="img" aria-label="Photograph of the golf clubhouse among trees with wooded hills behind and sand bunkers on the fairway in front"></div>
    <div class="frame"></div>

    <div class="sponsor sponsor--host">PRV</div>
    <div class="sponsor sponsor--wood"><span class="mark"></span>Tarnwell Wood</div>
    <div class="sponsor sponsor--acoustic">BSK</div>

    <h1 class="events band events-title">Events</h1>

    <section class="events event--golf">
      <div class="band event-head">
        <span class="event-name">Golf</span>
        <span class="event-sponsor">– Sponsored by Tarnwell Wood</span>
      </div>
      <div class="event-place">
        <svg viewBox="0 0 13 16"><path d="M6.5 0C2.9 0 0 2.8 0 6.3 0 10.8 6.5 16 6.5 16S13 10.8 13 6.3C13 2.8 10.1 0 6.5 0z M6.5 8.8a2.5 2.5 0 1 1 0-5 2.5 2.5 0 0 1 0 5z" fill="#fff" fill-rule="evenodd"/></svg>
        Fennock Golf Club, Surrey
      </div>
    </section>

    <section class="events event--offroad">
      <div class="band event-head">
        <span class="event-name">Off Road Adventure</span>
        <span class="event-sponsor">– Sponsored by BSK</span>
      </div>
      <div class="event-place">
        <svg viewBox="0 0 13 16"><path d="M6.5 0C2.9 0 0 2.8 0 6.3 0 10.8 6.5 16 6.5 16S13 10.8 13 6.3C13 2.8 10.1 0 6.5 0z M6.5 8.8a2.5 2.5 0 1 1 0-5 2.5 2.5 0 0 1 0 5z" fill="#fff" fill-rule="evenodd"/></svg>
        Fennock Golf Club, Surrey
      </div>
    </section>

    <section class="events closing">
      <p class="closing-details">Followed by Dinner and Overnight<br>Accommodation at Brimwell Manor<br>Hotel &amp; Country Club, Surrey.</p>
      <p class="closing-wish">We hope you will be able to join us.</p>
    </section>

    <p class="contact-phone">
      <svg viewBox="0 0 24 24"><path d="M6.6 10.8c1.4 2.8 3.8 5.1 6.6 6.6l2.2-2.2c.3-.3.7-.4 1-.2 1.1.4 2.3.6 3.6.6.6 0 1 .4 1 1V20c0 .6-.4 1-1 1C10.6 21 3 13.4 3 4c0-.6.4-1 1-1h3.5c.6 0 1 .4 1 1 0 1.3.2 2.5.6 3.6.1.3 0 .7-.2 1L6.6 10.8z" fill="#fff"/></svg>
      +44 (0) 20 7946 0817
    </p>
  </main>
</body>
</html>
```